Online-Marketing Material für ambulanter Pflegedienst
Zielgruppe
Unser Unternehmen, Lindenhof, ist ein ambulanter Pflegedienst, der sich darauf spezialisiert hat, individuelle und herzliche Pflege direkt in den eigenen vier Wänden unserer Klienten in Nürnberg und Umgebung anzubieten. Unser Hauptziel ist es, die Lebensqualität und Unabhängigkeit unserer Klienten zu fördern und zu erhalten, indem wir professionelle Pflege und Unterstützung bieten.
Unsere Dienstleistungen reichen von der häuslichen Krankenpflege über Palliative Care bis hin zur Beratung, wobei wir einen ganzheitlichen Ansatz verfolgen, um den individuellen Bedürfnissen und Wünschen jedes Klienten gerecht zu werden.
Unsere Zielgruppe sind vor allem ältere Menschen, die Unterstützung im Alltag benötigen, sowie Personen jeden Alters, die aufgrund von Krankheit oder Behinderung Pflege und Assistenz benötigen. Wir arbeiten eng mit den Familien unserer Klienten zusammen, um sicherzustellen, dass die von uns angebotene Pflege und Unterstützung auf die persönlichen Anforderungen und Vorlieben jedes Einzelnen abgestimmt ist.
Aufgabenstellung
Liebes Design-Team,
wir möchten eine Serie von Bannern erstellen lassen, die die Herzlichkeit und Fürsorge unseres ambulanten Pflegedienstes visualisieren. Jedes Banner soll einen anderen Schwerpunkt unserer Dienstleistungen präsentieren: Palliativpflege, Krankenpflege, Grundpflege sowie Betreuung und Hauswirtschaft.
Für die Gestaltung möchten wir gerne auf freundliche und liebevolle Vectorgrafiken setzen, die vor allem ältere und pflegebedürftige Menschen ansprechen. Die Botschaft sollte klar und einladend sein, um die Wärme und Unterstützung zu kommunizieren, die wir unseren Klienten täglich bieten.
Hier sind einige spezifische Anforderungen für jedes Banner:
Banner müssen für Plauderbox Werbung gestaltet werden. (940x788px) FREUNDLICHE UND RUNDE FORMEN sind erwünscht.
Banner 1: Palliativpflege - „Wo Fürsorge täglich aufgeht“
Untertitel: Fürsorgliche Hände, die in schwierigen Zeiten trösten
Spezialisierte Pflege für Schmerzmanagement und Symptomlinderung
Emotionaler Beistand und Unterstützung für Patienten und ihre Familien
Personalisierte Betreuung, die auf die Bedürfnisse jedes Einzelnen eingeht
Banner 2: Krankenpflege - „Wo Fürsorge täglich aufgeht“
Untertitel: Fachmännische Pflege, die Genesung unterstützt
Qualifizierte Krankenpflege und Medikamentenmanagement zu Hause
Professionelle Wundversorgung und nachoperative Pflege
Individuelle Pflegepläne zur Förderung der Gesundheit und des Wohlbefindens
Banner 3: Grundpflege - „Wo Fürsorge täglich aufgeht“
Untertitel: Tägliche Handreichungen, die das Leben erleichtern
Unterstützung bei der Körperpflege, Mobilität und Ernährung
Empathische Betreuung zur Bewahrung der Würde und Unabhängigkeit
Personalisierte Unterstützung, die das tägliche Leben erleichtert
Banner 4: Betreuung und Hauswirtschaft - „Wo Fürsorge täglich aufgeht“
Unte..

```html
<!DOCTYPE html>
<html lang="de">
<head>
<meta charset="utf-8">
<title>Lindenhof – Bannerserie</title>
<link rel="stylesheet" href="https://fonts.googleapis.com/css2?family=Dosis:wght@500;600&family=Didact+Gothic&family=Poppins:wght@500&display=swap">
<style>
  :root {
    --page: #ffffff;
    --banner-bg: #eef6fb;
    --soft-blue: #d6eaf6;
    --soft-yellow: #fde6b3;
    --orange: #f5a300;
    --blue: #2f6fb3;
    --blue-light: #3d86cc;
    --ink: #1b1b1b;
  }
  * { box-sizing: border-box; margin: 0; padding: 0; }
  html, body { width: 1200px; height: 1060px; overflow: hidden; background: var(--page); }
  .sheet { position: relative; width: 1200px; height: 1060px; }
  .banner {
    position: absolute; width: 510px; height: 427px;
    background: var(--banner-bg); border: 3px solid #fff;
    box-shadow: 0 2px 8px rgba(0,0,0,.22); overflow: hidden;
  }
  .b1 { left: 57px; top: 68px; } .b2 { left: 635px; top: 68px; }
  .b3 { left: 57px; top: 567px; } .b4 { left: 635px; top: 567px; }
  .deco { position: absolute; inset: 0; }
  .photo {
    position: absolute; left: 159px; top: 26px; width: 210px; height: 210px; border-radius: 50%;
  }
  .photo-tree { background: radial-gradient(circle at 45% 45%, #a9604a, #6e5646 55%, #b07a2c); }
  .photo-pressure { background: radial-gradient(circle at 60% 55%, #2c3440 0 22%, #e9dcd8 45%, #d8c8c4); }
  .photo-visit { background: linear-gradient(120deg, #e08a66 0 40%, #3b5e70 60%, #c9ccc8); }
  .photo-home { background: radial-gradient(circle at 62% 50%, #e7c7b0 0 25%, #f2ece6 55%, #d9c8b5); }
  .brand { position: absolute; left: 350px; top: 32px; width: 140px; display: flex; align-items: center; justify-content: center; gap: 5px; }
  .brand-dot { width: 9px; height: 9px; border-radius: 50%; background: var(--orange); }
  .brand-name { font-family: "Dosis", sans-serif; font-weight: 600; font-size: 20px; color: var(--blue); letter-spacing: .5px; }
  .copy { position: absolute; left: 0; right: 0; top: 258px; text-align: center; padding: 0 12px; }
  .title { font-family: "Dosis", sans-serif; font-weight: 600; font-size: 41px; line-height: 1; color: var(--orange); letter-spacing: 1px; }
  .title.long { font-size: 28px; padding: 6px 0 4px; }
  .claim { font-family: "Dosis", sans-serif; font-weight: 500; font-size: 18px; color: var(--blue-light); letter-spacing: .6px; margin-top: 2px; }
  .lead { font-family: "Poppins", sans-serif; font-weight: 500; font-size: 15px; color: var(--ink); margin-top: 7px; letter-spacing: -.4px; white-space: nowrap; }
  .body { font-family: "Didact Gothic", sans-serif; font-size: 12.8px; line-height: 16.5px; color: var(--ink); margin-top: 4px; }
</style>
</head>
<body>
<div class="sheet">

  <svg width="0" height="0" style="position:absolute">
    <defs>
      <g id="banner-deco">
        <circle cx="0" cy="0" r="65" fill="var(--soft-blue)"/>
        <polygon points="220,424 416,313 510,370 510,424" fill="var(--soft-blue)"/>
        <ellipse cx="30" cy="424" rx="55" ry="30" fill="var(--soft-yellow)"/>
        <g fill="var(--orange)">
          <circle cx="70" cy="185" r="1"/><circle cx="82" cy="185" r="1"/><circle cx="94" cy="185" r="1"/><circle cx="106" cy="185" r="1"/><circle cx="118" cy="185" r="1"/>
          <circle cx="70" cy="197" r="1"/><circle cx="82" cy="197" r="1"/><circle cx="94" cy="197" r="1"/><circle cx="106" cy="197" r="1"/><circle cx="118" cy="197" r="1"/>
          <circle cx="70" cy="209" r="1"/><circle cx="82" cy="209" r="1"/><circle cx="94" cy="209" r="1"/><circle cx="106" cy="209" r="1"/><circle cx="118" cy="209" r="1"/>
          <circle cx="70" cy="221" r="1"/><circle cx="82" cy="221" r="1"/><circle cx="94" cy="221" r="1"/><circle cx="106" cy="221" r="1"/><circle cx="118" cy="221" r="1"/>
        </g>
        <path d="M260 10 A121 119 0 0 0 260 248" fill="none" stroke="var(--blue)" stroke-width="3.5"/>
        <circle cx="260" cy="10" r="6" fill="var(--orange)"/>
        <circle cx="260" cy="248" r="6" fill="var(--blue-light)"/>
      </g>
    </defs>
  </svg>

  <section class="banner b1">
    <svg class="deco" viewBox="0 0 510 427"><use href="#banner-deco"/></svg>
    <div class="photo photo-tree" role="img" aria-label="Kinderhände umarmen einen Baumstamm mit gemaltem Herz"></div>
    <div class="brand"><span class="brand-dot"></span><span class="brand-name">LINDENHOF</span></div>
    <div class="copy">
      <h2 class="title">PALLIATIVPFLEGE</h2>
      <p class="claim">WO FÜRSORGE TÄGLICH AUFGEHT</p>
      <p class="lead">FÜRSORGLICHE HÄNDE, DIE IN SCHWIERIGEN ZEITEN TRÖSTEN</p>
      <p class="body">Spezialisierte Pflege für Schmerzmanagement und Symptomlinderung Emotionaler Beistand und Unterstützung für Patienten und ihre Familien Personalisierte Betreuung, die auf die Bedürfnisse jedes Einzelnen eingeht</p>
    </div>
  </section>

  <section class="banner b2">
    <svg class="deco" viewBox="0 0 510 427"><use href="#banner-deco"/></svg>
    <div class="photo photo-pressure" role="img" aria-label="Blutdruckmessung am Arm einer Patientin"></div>
    <div class="brand"><span class="brand-dot"></span><span class="brand-name">LINDENHOF</span></div>
    <div class="copy">
      <h2 class="title">KRANKENPFLEGE</h2>
      <p class="claim">WO FÜRSORGE TÄGLICH AUFGEHT</p>
      <p class="lead">FACHMÄNNISCHE PFLEGE, DIE GENESUNG UNTERSTÜTZT</p>
      <p class="body">Qualifizierte Krankenpflege und Medikamentenmanagement zu Hause Professionelle Wundversorgung und nachoperative Pflege Individuelle Pflegepläne zur Förderung der Gesundheit und des Wohlbefindens</p>
    </div>
  </section>

  <section class="banner b3">
    <svg class="deco" viewBox="0 0 510 427"><use href="#banner-deco"/></svg>
    <div class="photo photo-visit" role="img" aria-label="Pflegerin unterstützt einen älteren Herrn im Sessel"></div>
    <div class="brand"><span class="brand-dot"></span><span class="brand-name">LINDENHOF</span></div>
    <div class="copy">
      <h2 class="title">GRUNDPFLEGE</h2>
      <p class="claim">WO FÜRSORGE TÄGLICH AUFGEHT</p>
      <p class="lead">TÄGLICHE HANDREICHUNGEN, DIE DAS LEBEN ERLEICHTERN</p>
      <p class="body">Unterstützung bei der Körperpflege, Mobilität und Ernährung Empathische Betreuung zur Bewahrung der Würde und Unabhängigkeit Personalisierte Unterstützung, die das tägliche Leben erleichtert</p>
    </div>
  </section>

  <section class="banner b4">
    <svg class="deco" viewBox="0 0 510 427"><use href="#banner-deco"/></svg>
    <div class="photo photo-home" role="img" aria-label="Lächelnde Seniorin in ihrer Küche, im Hintergrund eine Haushaltshilfe"></div>
    <div class="brand"><span class="brand-dot"></span><span class="brand-name">LINDENHOF</span></div>
    <div class="copy">
      <h2 class="title long">BETREUUNG UND HAUSWIRTSCHAFT</h2>
      <p class="claim">WO FÜRSORGE TÄGLICH AUFGEHT</p>
      <p class="lead">IHR ZUHAUSE, LIEBEVOLL GEPFLEGT UNDORGANISIERT</p>
      <p class="body">Haushaltshilfe, Einkaufen und Mahlzeitenvorbereitung Organisation und Säuberung des Wohnraums zur Förderung einer angenehmen Umgebung Unterstützung bei täglichen Aufgaben für ein selbstbestimmtes Leben</p>
    </div>
  </section>

</div>
</body>
</html>
```